Brightfernrx website

We are a weight loss clinic and we need a website built. please look at these websites for content and style. Just need like 5 pages see samples. AI files of logo are not avail yet so use sample for place set

https://glowshiftstudio.com/
ortanvital.com
https://pinecrestclinicalbodybalance.com/
https://yourslimmingnook.com/
https://qrvskinstudio.com/treatments/weight-loss-injections/

Target Market(s)

Women

Industry/Entity Type

weight loss

Coding

Coded - Design and coding required

Number of Pages Required

5+ page

Requirements
Nice to have
• please make look like a medspa website

```html
<!DOCTYPE html>
<html lang="en">
<head>
<meta charset="utf-8">
<title>Brightfernrx — Classes &amp; Schedule</title>
<link href="https://fonts.googleapis.com/css2?family=Lustria&family=Open+Sans:wght@400;600&display=swap" rel="stylesheet">
<style>
:root{
  --page:#f2f4f3;
  --mint:#cfe8dc;
  --mint-soft:#e4f1ea;
  --green:#1d5a3e;
  --green-text:#2c6a4b;
  --gold:#d49e2a;
  --rule:#d9dedb;
  --white:#ffffff;
  --footer:#1c5a3d;
}
*{box-sizing:border-box;margin:0;padding:0}
html,body{width:1200px;height:3783px;overflow:hidden}
body{position:relative;background:var(--page);font-family:"Open Sans",sans-serif;color:var(--green)}
.hero{position:absolute;left:0;top:0;width:1200px;height:500px;
  background:radial-gradient(ellipse 520px 330px at 600px 240px,#bfe1d2 0%,#d3ebe0 45%,rgba(242,244,243,0) 100%),linear-gradient(180deg,#d4ebe0 0%,#dcefe6 55%,var(--page) 100%)}
.nav{position:absolute;top:0;left:0;width:1200px;height:76px}
.nav a{position:absolute;top:30px;font-size:12.5px;letter-spacing:.3px;color:var(--green);text-decoration:none;text-transform:uppercase;transform:translateX(-50%)}
.nav a.active{color:#3d9a6a}
.nav a.book{color:var(--gold)}
.brand{position:absolute;top:24px;left:588px;transform:translateX(-50%);display:flex;align-items:center;gap:8px;font-family:"Lustria",serif;font-size:24px;color:#2f7fa8}
.brand i{display:block;width:22px;height:22px;border-radius:50%;background:#7bb64a}
.hero h1{position:absolute;top:248px;left:0;width:1200px;text-align:center;font-family:"Lustria",serif;font-weight:400;font-size:43px;line-height:50px;color:var(--green)}
.class{position:absolute;left:167px;width:866px;height:735px}
.class .photo{position:absolute;left:0;top:0;width:866px;height:349px}
.class h2{position:absolute;left:12px;top:393px;font-family:"Lustria",serif;font-weight:400;font-size:33px;color:var(--green)}
.class p{position:absolute;left:12px;top:455px;width:270px;font-size:12.5px;line-height:21px;color:var(--green-text)}
.class .btn{position:absolute;left:12px;top:545px;width:137px;height:39px;background:var(--gold);color:#fff;font-size:12px;line-height:39px;text-align:center;text-decoration:none}
.schedule{position:absolute;left:366px;top:318px;width:487px;height:395px;background:var(--white);box-shadow:0 6px 18px rgba(30,60,45,.12)}
.schedule h3{position:absolute;top:34px;width:100%;text-align:center;font-family:"Lustria",serif;font-weight:400;font-size:21px;color:var(--green)}
.schedule table{position:absolute;left:25px;top:82px;width:438px;border-collapse:collapse;font-size:11.5px;color:var(--green-text);text-align:center}
.schedule th{height:38px;font-weight:600;font-size:11.5px;color:var(--green);border-bottom:1px solid var(--rule)}
.schedule td{height:59.5px;line-height:20px;border-bottom:1px solid var(--rule)}
.schedule tr:last-child td{border-bottom:none}
.schedule th+th,.schedule td+td{border-left:1px solid var(--rule)}
.schedule td.time{width:94px;color:var(--gold);font-weight:600}
.ornament{position:absolute;left:483px;top:2980px;width:234px;height:245px;border-radius:50%;background:radial-gradient(circle,#e6b64a 0%,#d49e2a 70%,rgba(212,158,42,.0) 72%)}
.footer-band{position:absolute;left:0;top:3200px;width:1200px;height:190px;background:linear-gradient(180deg,var(--page) 0%,var(--mint-soft) 45%,var(--mint) 100%)}
.footer-band svg{position:absolute;left:0;bottom:0}
.footer{position:absolute;left:0;top:3383px;width:1200px;height:400px;background:radial-gradient(ellipse 520px 260px at 600px 200px,#24684a 0%,var(--footer) 100%)}
.footer p{position:absolute;left:0;width:1200px;text-align:center;font-family:"Lustria",serif;color:#e8f1ec}
.footer .tag{top:208px;font-size:15.5px}
.footer .contact{top:233px;font-size:13px}
.footer .up{position:absolute;left:1008px;top:364px}
</style>
</head>
<body>
<header class="hero">
  <nav class="nav">
    <a href="#" style="left:239px">Home</a>
    <a href="#" class="active" style="left:321px">Services</a>
    <a href="#" style="left:418px">Pricing</a>
    <div class="brand"><i></i>Brightfernrx</div>
    <a href="#" style="left:758px">About</a>
    <a href="#" style="left:843px">Contact</a>
    <a href="#" class="book" style="left:967px">Book Online</a>
  </nav>
  <h1>The natural way of gaining<br>a perfect body &amp; mind</h1>
</header>

<section class="class" style="top:543px">
  <div class="photo" role="img" aria-label="Hands rolling up a green yoga mat on a wooden floor" style="background:linear-gradient(100deg,#6e625a 0%,#c9b9a6 30%,#2f9a78 60%,#e8ebe8 100%)"></div>
  <h2>Lorem Pei</h2>
  <p>Aliquam ac dui vel dui vulputate consectetur. Mauris accumsan, massa non consectetur condimentum.</p>
  <a href="#" class="btn">View more details</a>
  <div class="schedule">
    <h3>Schedule 2023</h3>
    <table>
      <tr><th></th><th>Mon</th><th>Wed</th><th>Fri</th></tr>
      <tr><td class="time">2:00 am</td><td>Basic<br>Group A</td><td>-</td><td>-</td></tr>
      <tr><td class="time">4:00 am</td><td>-</td><td>Basic<br>Group A</td><td>Basic<br>Group B</td></tr>
      <tr><td class="time">6:00 am</td><td>-</td><td>Basic<br>Group A</td><td>-</td></tr>
      <tr><td class="time">8:00 am</td><td>Basic<br>Group A</td><td>-</td><td>Basic<br>Group B</td></tr>
    </table>
  </div>
</section>

<section class="class" style="top:1348px">
  <div class="photo" role="img" aria-label="Woman in a black leotard stretching on the floor against a pale wall" style="background:linear-gradient(180deg,#dfe5e3 0%,#d2dad8 60%,#c6cfcc 100%)"></div>
  <h2>Lorem Pei</h2>
  <p>Aliquam ac dui vel dui vulputate consectetur. Mauris accumsan, massa non consectetur condimentum.</p>
  <a href="#" class="btn">View more details</a>
  <div class="schedule">
    <h3>Schedule 2023</h3>
    <table>
      <tr><th></th><th>Mon</th><th>Wed</th><th>Fri</th></tr>
      <tr><td class="time">2:00 am</td><td>Basic<br>Group A</td><td>-</td><td>-</td></tr>
      <tr><td class="time">4:00 am</td><td>-</td><td>Basic<br>Group A</td><td>Basic<br>Group B</td></tr>
      <tr><td class="time">6:00 am</td><td>-</td><td>Basic<br>Group A</td><td>-</td></tr>
      <tr><td class="time">8:00 am</td><td>Basic<br>Group A</td><td>-</td><td>Basic<br>Group B</td></tr>
    </table>
  </div>
</section>

<section class="class" style="top:2153px">
  <div class="photo" role="img" aria-label="Two women doing plank exercises on a blue mat by the waterfront" style="background:linear-gradient(180deg,#8ea3b3 0%,#b7c2c9 40%,#9b7a6c 75%,#a5796a 100%)"></div>
  <h2>Lorem Pei</h2>
  <p>Aliquam ac dui vel dui vulputate consectetur. Mauris accumsan, massa non consectetur condimentum.</p>
  <a href="#" class="btn">View more details</a>
  <div class="schedule">
    <h3>Schedule 2023</h3>
    <table>
      <tr><th></th><th>Mon</th><th>Wed</th><th>Fri</th></tr>
      <tr><td class="time">2:00 am</td><td>Basic<br>Group A</td><td>-</td><td>-</td></tr>
      <tr><td class="time">4:00 am</td><td>-</td><td>Basic<br>Group A</td><td>Basic<br>Group B</td></tr>
      <tr><td class="time">6:00 am</td><td>-</td><td>Basic<br>Group A</td><td>-</td></tr>
      <tr><td class="time">8:00 am</td><td>Basic<br>Group A</td><td>-</td><td>Basic<br>Group B</td></tr>
    </table>
  </div>
</section>

<div class="ornament" role="img" aria-label="Golden circular ornament of leafy branches"></div>

<div class="footer-band">
  <svg width="1200" height="60" viewBox="0 0 1200 60" aria-hidden="true">
    <path d="M0 60 L545 60 Q590 58 597 18 L600 10 L603 18 Q610 58 655 60 L1200 60 Z" fill="var(--footer)"/>
  </svg>
</div>

<footer class="footer">
  <p class="tag">Nullam viverra consectetuer quisque cursus et, porttitor risus.</p>
  <p class="contact">+61 (0) 3000000000 info@yourdomain.com</p>
  <svg class="up" width="14" height="9" viewBox="0 0 14 9" aria-hidden="true"><path d="M1 8 L7 2 L13 8" fill="none" stroke="#5e8f76" stroke-width="1.3"/></svg>
</footer>
</body>
</html>
```